Business Card Design Project

I need a cool business card design for the company that will build residential houses.
The card should include:
1) Name: Boris Kalinov
2) Cell: 587.204.XXXX
3) Email: bor.kalinov@qwvend.example
4) Position: General Manager
5) Residential Home Building
6) Company logo that I have uploaded

Industry/Entity Type

Residential

```html
<!DOCTYPE html>
<html lang="en">
<head>
<meta charset="utf-8">
<title>Qwvend Developments – Business Card</title>
<link rel="stylesheet" href="https://fonts.googleapis.com/css2?family=Open+Sans:wght@400;700&family=Questrial&display=swap">
<style>
  :root {
    --bg: #e9ecef;
    --card-white: #fbfbfa;
    --brand-blue: #1f5aa6;
    --deep-blue: #0d3f94;
    --bright-blue: #1a6bc4;
    --brand-green: #6cc117;
    --ink: #333333;
    --ink-soft: #555555;
    --divider: #c9c9c9;
  }
  * { box-sizing: border-box; margin: 0; padding: 0; }
  html, body { width: 1200px; height: 800px; overflow: hidden; }
  body {
    background: var(--bg);
    font-family: "Open Sans", Arial, sans-serif;
    position: relative;
  }
  .card {
    position: absolute;
    left: 290px;
    width: 620px;
    height: 354px;
    overflow: hidden;
    box-shadow: 0 6px 18px rgba(0,0,0,0.15);
  }
  .card--front { top: 30px; background: var(--card-white); }
  .card--back {
    top: 416px;
    background: linear-gradient(135deg, var(--bright-blue) 0%, var(--deep-blue) 100%);
    color: #ffffff;
  }

  /* Front */
  .company-mark {
    position: absolute;
    left: 40px; top: 142px;
    display: flex; align-items: center; gap: 10px;
    white-space: nowrap;
  }
  .company-mark__dot {
    width: 18px; height: 18px; border-radius: 50%;
    background: var(--brand-green);
  }
  .company-mark__name {
    font-family: "Open Sans", Arial, sans-serif;
    font-weight: 700;
    font-size: 20px;
    color: var(--brand-blue);
    letter-spacing: 0.3px;
  }
  .front-divider {
    position: absolute; left: 340px; top: 78px;
    width: 1px; height: 118px; background: var(--divider);
  }
  .person { position: absolute; left: 368px; top: 86px; white-space: nowrap; }
  .person__name {
    font-weight: 700; font-size: 19px; color: var(--ink); letter-spacing: 0.5px;
  }
  .person__role { font-size: 13px; color: var(--ink-soft); margin-top: 2px; margin-left: 4px; }
  .contacts { list-style: none; margin-top: 22px; margin-left: 12px; }
  .contacts li {
    display: flex; align-items: center; gap: 12px;
    font-size: 13px; color: var(--ink); margin-bottom: 6px;
  }
  .contacts svg { width: 14px; height: 14px; flex: none; }
  .tagline {
    position: absolute; left: 34px; top: 292px;
    font-family: "Questrial", Arial, sans-serif;
    font-size: 18px; color: var(--brand-green); letter-spacing: 0.3px;
    white-space: nowrap;
  }
  .front-bands { position: absolute; left: 0; top: 0; width: 620px; height: 354px; }

  /* Back */
  .back-watermark {
    position: absolute; left: 0; right: 0; top: 150px; text-align: center;
    font-family: "Questrial", Arial, sans-serif;
    font-size: 34px; letter-spacing: 1px;
    color: rgba(255,255,255,0.16);
    white-space: nowrap;
  }
  .back-contacts { position: absolute; left: 46px; top: 268px; list-style: none; }
  .back-contacts li {
    display: flex; align-items: center; gap: 14px;
    font-size: 13px; color: #ffffff; margin-bottom: 6px;
    white-space: nowrap;
  }
  .back-contacts svg { width: 14px; height: 14px; flex: none; }
  .back-divider {
    position: absolute; left: 330px; top: 246px;
    width: 1px; height: 70px; background: rgba(255,255,255,0.45);
    transform: rotate(-28deg);
  }
  .back-person { position: absolute; left: 372px; top: 262px; white-space: nowrap; }
  .back-person__name { font-weight: 700; font-size: 19px; letter-spacing: 0.5px; }
  .back-person__role { font-size: 13px; margin-top: 2px; margin-left: 40px; opacity: 0.9; }
  .back-edge {
    position: absolute; left: 0; right: 0; bottom: 0; height: 8px;
    background: rgba(255,255,255,0.18);
  }
</style>
</head>
<body>

<section class="card card--front" aria-label="Business card front">
  <svg class="front-bands" viewBox="0 0 620 354" aria-hidden="true">
    <polygon points="388,316 620,268 620,306 380,340" fill="var(--brand-green)"/>
    <polygon points="0,336 372,318 364,342 0,354" fill="var(--brand-blue)"/>
  </svg>

  <div class="company-mark">
    <span class="company-mark__dot"></span>
    <span class="company-mark__name">Qwvend Developments</span>
  </div>

  <div class="front-divider"></div>

  <div class="person">
    <h1 class="person__name">BORIS KALINOV</h1>
    <p class="person__role">General Manager</p>
    <ul class="contacts">
      <li>
        <svg viewBox="0 0 14 14" aria-hidden="true"><rect x="3.5" y="0.8" width="7" height="12.4" rx="1.4" fill="none" stroke="var(--brand-blue)" stroke-width="1.4"/><circle cx="7" cy="10.8" r="0.9" fill="var(--brand-blue)"/></svg>
        587.204.XXXX
      </li>
      <li>
        <svg viewBox="0 0 14 14" aria-hidden="true"><rect x="0.5" y="2.5" width="13" height="9" fill="var(--brand-blue)"/><polyline points="0.8,3 7,8 13.2,3" fill="none" stroke="#ffffff" stroke-width="1.1"/></svg>
        bor.kalinov@qwvend.example
      </li>
    </ul>
  </div>

  <p class="tagline">RESIDENTIAL HOME BUILDING</p>
</section>

<section class="card card--back" aria-label="Business card back">
  <p class="back-watermark">RESIDENTIAL HOME BUILDING</p>

  <ul class="back-contacts">
    <li>
      <svg viewBox="0 0 14 14" aria-hidden="true"><rect x="3.5" y="0.8" width="7" height="12.4" rx="1.4" fill="none" stroke="#ffffff" stroke-width="1.4"/><circle cx="7" cy="10.8" r="0.9" fill="#ffffff"/></svg>
      587.204.XXXX
    </li>
    <li>
      <svg viewBox="0 0 14 14" aria-hidden="true"><rect x="0.5" y="2.5" width="13" height="9" fill="#ffffff"/><polyline points="0.8,3 7,8 13.2,3" fill="none" stroke="var(--deep-blue)" stroke-width="1.1"/></svg>
      bor.kalinov@qwvend.example
    </li>
  </ul>

  <div class="back-divider"></div>

  <div class="back-person">
    <h2 class="back-person__name">BORIS KALINOV</h2>
    <p class="back-person__role">General Manager</p>
  </div>

  <div class="back-edge"></div>
</section>

</body>
</html>
```